Romantic Comedy Film Needs a Cool Poster

Need a professional looking poster for our film called Mabel Sunstruck. The film is a romantic comedy about a guy who makes himself allergic to his girlfriend. I'm not sure quite what I want the poster to look like but I've included a few images of Mabel (the main character) so do what you think would look best, even cutting the backgrounds out is encouraged if you have a good vision. It just has to say "Mabel Sunstruck", and that can be in all caps or whatever you think looks best. I'm even open to not using any of the pictures if you can come up with a design that looks good. Note: I probably don't want to use the words "bang bang" in the poster as it will be too distracting, but if you think it would work go for it.
The film is black and white, so keep this in mind when making your poster design. The main inspiration for the film is another film called 'Odile Brun'
The final poster file has to follow standard poster print spec and resolution requirements as we will be printing it large as well submitting the file to film festivals. If the images I've provided are too small to achieve this, just make them a little bigger, I don't mind too much if it looks good.
Any questions, just let me know. Thank you for your time! :)
Industry/Entity Type
Film Production
Font styles to use
Other font styles liked:
- No preference. Probably sans serif, but looking at the poster for the film Odile Brun, Serif seems to work. Go with your judgement.
Colors
Designer to choose colors to be used in the design.
Requirements
Must have
- Must have the title Mabel Sunstruck on the poster without any line break between the words "sun" and "struck". Any capitalisation and font, but the only variation we don't want is "Mabel SunStruck" because "Sunstruck" needs to be conveyed as one word.
Nice to have
- The actual film is entirely black and white, so keep this in mind with your designs. You might want to keep the poster entirely black and white, or even just duller colours. What could maybe work best is just one single colour in addition to the black and white. Search up the Odile Brun poster to see an example of the one extra colour standing out. But I'm not against any colours or ideas.
- The tagline for the film is: His mind is telling him yes, but his body is telling him no.
- Only include this if you think it works well.
Should not have
- There must not be a line break between "sun" and "struck".

```html
<!DOCTYPE html>
<html lang="en">
<head>
<meta charset="utf-8">
<title>Mabel Sunstruck — Poster</title>
<link rel="stylesheet" href="https://fonts.googleapis.com/css2?family=Kaushan+Script&family=Libre+Baskerville&family=Oswald:wght@300;400&display=swap">
<style>
  :root {
    --paper: #f5b8c8;
    --ink: #6a1052;
    --ink-soft: #a9507f;
    --photo-light: #c27a9f;
    --photo-dark: #5c0d47;
  }
  * { margin: 0; padding: 0; box-sizing: border-box; }
  html, body { width: 803px; height: 1200px; overflow: hidden; background: var(--paper); }
  .poster {
    position: relative;
    width: 803px;
    height: 1200px;
    background: var(--paper);
    color: var(--ink);
    overflow: hidden;
  }
  .byline {
    position: absolute;
    top: 80px; left: 0; width: 100%;
    text-align: center;
    font-family: "Libre Baskerville", serif;
    font-size: 16px;
    letter-spacing: 2.5px;
  }
  .title {
    position: absolute;
    top: 118px; left: 0; width: 100%;
    font-family: "Kaushan Script", cursive;
    font-weight: 400;
    line-height: 1;
    color: var(--ink);
  }
  .title .first { display: block; margin-left: 210px; font-size: 104px; }
  .title .last { display: block; margin-left: 298px; margin-top: -18px; font-size: 96px; white-space: nowrap; }
  .tagline {
    position: absolute;
    top: 350px; left: 0; width: 100%;
    text-align: center;
    font-family: "Libre Baskerville", serif;
    font-size: 19px;
    letter-spacing: 1.6px;
  }
  .credits {
    position: absolute;
    top: 392px; left: 0; width: 100%;
    text-align: center;
    font-family: "Oswald", sans-serif;
    font-weight: 300;
    color: var(--ink-soft);
    font-size: 15px;
    line-height: 23px;
    letter-spacing: 0.3px;
    text-transform: uppercase;
  }
  .credits .role { font-size: 9px; letter-spacing: 0.6px; }
  .portrait {
    position: absolute;
    left: 22px; top: 565px;
    width: 758px; height: 635px;
    border-radius: 300px 300px 0 0;
    background: radial-gradient(ellipse at 50% 35%, var(--photo-light) 0%, var(--photo-dark) 75%);
  }
</style>
</head>
<body>
<main class="poster">
  <p class="byline">a film by OWEN MARLOWE</p>
  <h1 class="title"><span class="first">Mabel</span><span class="last">Sunstruck</span></h1>
  <p class="tagline">His mind is telling him yes, but his body is telling him no.</p>
  <div class="credits">
    <div>"Mabel Sunstruck" <span class="role">starring</span> Owen Marlowe &nbsp;Tessa Quill <span class="role">and</span> Milo Brandt &nbsp;<span class="role">edited by</span> Dane Holloway</div>
    <div><span class="role">music by</span> Rui Tan Seng &nbsp;<span class="role">sound designer</span> Ezra Whitlock &nbsp;<span class="role">production designer</span> Nora Ashby &nbsp;<span class="role">director of photography</span> Lena Park</div>
    <div><span class="role">produced by</span> Felix Harrow &nbsp;Ivy Castellan &nbsp;<span class="role">written and directed by</span> Owen Marlowe</div>
  </div>
  <div class="portrait" role="img" aria-label="Duotone portrait of the lead actor in a dark hoodie, a tissue tucked in his nose, looking worried at the viewer"></div>
</main>
</body>
</html>
```